Infografik für unabhängigen Finanzdienstleister
Zielgruppe
Wir sind eine unabhängiger Finanzdienstleister mit dem Schwerpunkt der Kapitalanlage und dem Fokus auf vermögende Privatkunden. Wir sind nur unseren Mandanten verpflichtet, da diese unsere Dienstleistung transparent und frei von versteckten Provisionen honorieren.
Aufgabenstellung
Klassisch modern, aber nicht verspielt. Ein Gefühl gibt unsere Homepage. Weitere Infos zum Projekt habe ich hier in einem kurzen Video verfasst: https://lobark.vemiko-kanzlei.example/message?id=7f91c3a5e2d04b
Ergänzung:
Die Grafik soll sich mehr 'selbst erklären lassen' als sie es derzeit tut. Zudem soll die Prozessreihenfolge besser verdeutlicht werden...

```html
<!DOCTYPE html>
<html lang="de">
<head>
<meta charset="utf-8">
<title>Infografik Finanzberatung</title>
<link rel="stylesheet" href="https://fonts.googleapis.com/css2?family=Lexend:wght@400;700&family=Courier+Prime:wght@700&display=swap">
<style>
  :root {
    --ink: #1f1e20;
    --hex-dark: #2e2d2f;
    --gold-1: #b0892f;
    --gold-2: #c4a25a;
    --gold-3: #d3bb85;
    --paper: #ffffff;
    --icon-fill: #3a393b;
  }
  * { margin: 0; padding: 0; box-sizing: border-box; }
  html, body { width: 1200px; height: 574px; overflow: hidden; background: var(--paper); }
  .canvas { position: relative; width: 1200px; height: 574px; font-family: "Lexend", sans-serif; color: var(--ink); }
  .shapes { position: absolute; inset: 0; }
  .hex-label {
    position: absolute; color: #fff; font-size: 14.2px; line-height: 19.4px; font-weight: 400;
  }
  .row { position: absolute; left: 0; width: 1200px; height: 108px; }
  .cell { position: absolute; top: 0; height: 108px; display: flex; align-items: center; font-size: 14.2px; line-height: 19.4px; }
  .numeral { font-family: "Courier Prime", monospace; font-weight: 700; font-size: 18px; letter-spacing: 1px; }
  .step-title { font-weight: 700; font-size: 15.5px; line-height: 21px; }
</style>
</head>
<body>
<div class="canvas">
  <svg class="shapes" width="1200" height="574" viewBox="0 0 1200 574">
    <!-- benefit hexagons -->
    <polygon fill="var(--hex-dark)" points="205,59 284,101 284,188 205,229 126,188 126,101"/>
    <polygon fill="var(--hex-dark)" points="291,198 370,240 370,326 291,368 212,326 212,240"/>
    <polygon fill="var(--hex-dark)" points="207,339 286,381 286,466 207,508 128,466 128,381"/>
    <polygon fill="none" stroke="var(--hex-dark)" stroke-width="2" points="121,202 199,244 199,328 121,370 43,328 43,244"/>
    <rect x="72" y="240" width="98" height="84" rx="6" fill="var(--icon-fill)" role="img" aria-label="Symbol: Berater mit Aktentasche"/>

    <!-- step I -->
    <polyline points="405,104 435,147 405,190" fill="none" stroke="var(--gold-1)" stroke-width="3"/>
    <path d="M647,94.5 H1100 Q1153,94.5 1153,147 Q1153,199.5 1100,199.5 H647" fill="none" stroke="var(--gold-1)" stroke-width="2.5"/>
    <polygon fill="var(--gold-1)" points="419,93 647,93 647,201 419,201 453,147"/>

    <!-- step II -->
    <polyline points="405,244 435,287 405,330" fill="none" stroke="var(--gold-2)" stroke-width="3"/>
    <path d="M647,234.5 H1100 Q1153,234.5 1153,287 Q1153,339.5 1100,339.5 H647" fill="none" stroke="var(--gold-2)" stroke-width="2.5"/>
    <polygon fill="var(--gold-2)" points="419,233 649,233 649,341 419,341 453,287"/>

    <!-- step III -->
    <polyline points="406,386 436,429 406,472" fill="none" stroke="var(--gold-3)" stroke-width="3"/>
    <path d="M647,376.5 H1100 Q1153,376.5 1153,429 Q1153,481.5 1100,481.5 H647" fill="none" stroke="var(--gold-3)" stroke-width="2.5"/>
    <polygon fill="var(--gold-3)" points="419,375 649,375 649,483 419,483 453,429"/>
  </svg>

  <div class="hex-label" style="left:162px; top:107px;">Finanzieller<br>Erfolg/gute<br>Investment<br>Erfahrung</div>
  <div class="hex-label" style="left:250px; top:255px;">Weniger<br>Verwaltung,<br>mehr Zeit</div>
  <div class="hex-label" style="left:161px; top:387px;">Umfassender<br>Schutz von<br>Vermögen<br>und Familie</div>

  <div class="row" style="top:93px;">
    <div class="cell numeral" style="left:470px;">I.</div>
    <div class="cell step-title" style="left:527px;">Starkes<br>Fundament</div>
    <div class="cell" style="left:666px;">Entwicklung eines<br>persönlichen<br>Finanzplanes</div>
    <div class="cell" style="left:847px;">Wissens-<br>vermittlung</div>
    <div class="cell" style="left:997px;">Tiefe Analyse Ihrer<br>IST-Situation und<br>Ihrer Ziele</div>
  </div>

  <div class="row" style="top:233px;">
    <div class="cell numeral" style="left:470px;">II.</div>
    <div class="cell step-title" style="left:527px;">Nachhaltige<br>Umsetzung</div>
    <div class="cell" style="left:666px;">Nobelpreisgekrönte<br>und erfolgreiche<br>Anlagestrategie</div>
    <div class="cell" style="left:845px;">Berücksichtigung<br>steuerlicher<br>Aspekte</div>
    <div class="cell" style="left:1008px;">Transparente<br>und provisions-<br>freie Vergütung</div>
  </div>

  <div class="row" style="top:375px;">
    <div class="cell numeral" style="left:467px;">III.</div>
    <div class="cell step-title" style="left:524px;">Aktive Beglei-<br>tung und<br>Optimierung</div>
    <div class="cell" style="left:674px;">Zentraler Ansprech-<br>partner zum Thema<br>Finanzen</div>
    <div class="cell" style="left:865px;">Notfallplan</div>
    <div class="cell" style="left:1013px;">Experten-<br>Netzwerk</div>
  </div>
</div>
</body>
</html>
```